A Writer With A Website (Writes action/mysteries with a touch of romance thrown in)

I need a website. I am an unpublished writer. I own a domain and tried a bit to design one in Wordpress. I would like to be able to change out pictures, blog, and receive email. My fav color is orange (but not necessary in website) I like the font "Hello Stockholm" Probably 4 or five different pages. Attached is a poor scan of a business card.
Updates

Had a recent death in the family, my inspiration to get the site designed and also the reason I may need a few days.

I write books action mysteries. So far all take place in Wyoming. I realize there was not much info given. Pages: Home, Looking for representation, recommended reading and other things I like, Mirabel (a page dedicated to my daughter who just passed away), and other useful links. Probably shorter ways to say those, but you get the idea.

Thanks for the designs submitted. I know I gave very little direction. There are a few authors who write in Wyoming who are popular, RT Haskell, Dwight Fenner (Ashcroft Saga) I would argue that the main character in any of their books is Wyoming, or the West. No cliches. Cowboy hats, horses, not so good. For those outside the US, maybe do a serch on Wyoming and look at the pictures. I have photo's for possible use in my design, will post them tonight. Thanks all. -k-

I am not sure how much info gets added, how much the designer does and how I fill in the "blanks". Here is partial text for the "Mirabel" page: Over the years, our daughters’ friends overlapped one another and two or three became like daughters to Loreen and me. Some even became our friends as they grew into adulthood. One had a father who tried to committed suicide multiple times. After one attempt she asked him, “why?” He said, “I am glad you can’t understand why, only someone who can travel to that dark a place can understand why”. He was eventually successful. She shared that story with us on August 14th when our daughter Mirabel found that dark place in herself and took her life. We found a suicide note, then her body, then everything went into a fog. An hour or so later, my wife and I stood on the front lawn after the police interviews and watched as the corner slide a covered corpse into the white SUV with darkened windows. We stood there as the rain began to fall, and the sky sobbed with us. As they closed the back of the coroner’s Suburban, the rain fell harder and harder and a fireman guided us back into the house that will never be the same for us.

Target Market(s)

Currently trying to get an agent, this is to look like I have followers.

Number of Pages Required

5+ page

Font styles to use
Serif

Colors
f68e4e

Requirements
Nice to have
• I like orange (more of a burnt orange color) I am a big fan of Matthias Dorrel. A "feel" like that might be nice. I am from Wyoming, That rugged western culture shows up in all my writing.
Should not have
• Western Cliche,

```html
<!DOCTYPE html>
<html lang="en">
<head>
<meta charset="utf-8">
<title>Everett Lane Corbin — Author</title>
<link href="https://fonts.googleapis.com/css2?family=Kaushan+Script&family=Josefin+Sans:wght@400;600&family=EB+Garamond:wght@400;600&display=swap" rel="stylesheet">
<style>
:root{
  --ink:#2a2118;
  --ink-soft:#5b4a36;
  --body:#6e5c48;
  --white:#ffffff;
  --about-bg:#e9d98c;
  --welcome-bg:#ecd497;
  --pale-bg:#ebe7b4;
  --tan-bg:#e8b680;
  --footer-bg:#9c8640;
  --footer-band:#c9ab3c;
  --rule:#4a3d2c;
}
*{margin:0;padding:0;box-sizing:border-box}
html,body{width:1200px;height:3593px;overflow:hidden}
body{position:relative;font-family:"EB Garamond",Georgia,serif;color:var(--body);background:var(--about-bg)}
.abs{position:absolute}
.script{font-family:"Kaushan Script",cursive;color:var(--ink);font-weight:400}
.label{font-family:"Josefin Sans",Arial,sans-serif;text-transform:uppercase;letter-spacing:1px;color:var(--ink-soft);font-size:19px}
.text{font-size:16.5px;line-height:27px;color:var(--body)}
.photo{position:absolute;box-shadow:0 2px 8px rgba(0,0,0,.35)}

/* hero */
.hero{top:0;left:0;width:1200px;height:700px;
  background:linear-gradient(180deg,#f2c54a 0%,#f0a33e 10%,#d9708a 20%,#8b7bb0 28%,#dfe6f3 33%,#3d4660 40%,#1d2230 45%,#c85a2a 58%,#f39a3a 70%,#d86f2c 82%,#5d3a2e 100%)}
.logo{left:50px;top:52px;font-size:42px;color:var(--ink);white-space:nowrap}
.nav{top:72px;left:620px;display:flex;gap:38px;font-family:"Josefin Sans",sans-serif;font-weight:600;font-size:16px;letter-spacing:1.5px;color:var(--ink)}
.hero-title{left:110px;top:340px;font-size:96px;color:var(--white);line-height:1.05;transform:rotate(-7deg);transform-origin:left top}
.hero-title span{display:block;padding-left:175px}

/* about */
.about{top:700px;left:0;width:1200px;height:570px;background:linear-gradient(180deg,#eadb8a 0%,#e4d796 50%,#c9c6a8 100%)}
.rule{height:2px;background:var(--rule)}

/* welcome */
.welcome{top:1270px;left:0;width:1200px;height:360px;background:var(--welcome-bg)}
.welcome h2{position:absolute;top:60px;width:100%;text-align:center;font-size:60px;letter-spacing:4px}
.welcome p{position:absolute;top:158px;left:170px;width:860px;text-align:center;font-size:15px;line-height:25px;color:var(--ink);font-weight:600}
.more{font-family:"EB Garamond",serif;font-weight:600;font-size:15px;letter-spacing:1px;color:var(--ink)}

/* pale */
.pale{top:1630px;left:0;width:1200px;height:545px;background:var(--pale-bg)}
.quote{font-size:21px;line-height:44px;color:var(--ink)}

/* dusk */
.dusk{top:2175px;left:0;width:1200px;height:582px;background:linear-gradient(100deg,#3b2c22 0%,#8a6a45 35%,#c89b5c 55%,#6b5236 80%,#2f2a20 100%)}
.dusk .label{color:var(--white);font-size:20px}
.dusk .text{color:#efe2c8}

/* tan */
.tan{top:2757px;left:0;width:1200px;height:513px;background:var(--tan-bg)}

/* footer */
.band{top:3270px;left:0;width:1200px;height:20px;background:var(--footer-band)}
.footer{top:3290px;left:0;width:1200px;height:303px;background:var(--footer-bg);color:var(--white)}
.footer .logo{left:50px;top:66px;color:var(--white);font-size:38px}
.fhead{font-family:"EB Garamond",serif;font-weight:600;font-size:16px;color:var(--white)}
.flist{font-family:"EB Garamond",serif;font-weight:600;font-size:13px;line-height:20px;text-transform:uppercase;color:var(--white);list-style:none}
.ftext{font-size:13px;line-height:20px;font-weight:600;color:var(--white)}
</style>
</head>
<body>

<header class="abs hero" role="img" aria-label="Snow-capped mountains reflected in a lake at sunset">
  <div class="abs logo script">Everett Lane Corbin</div>
  <nav class="abs nav"><span>LITERATURE</span><span>WRITING</span><span>ABOUT ME</span><span>CONTACT</span></nav>
  <h1 class="abs hero-title script">Can you guess<span>the mystery?</span></h1>
</header>

<section class="abs about">
  <h2 class="abs script" style="left:85px;top:40px;font-size:62px;letter-spacing:4px">About me</h2>
  <div class="photo" role="img" aria-label="Reading glasses on an open notebook with old photographs" style="left:88px;top:162px;width:264px;height:348px;background:linear-gradient(160deg,#3d3024 0%,#8a7458 55%,#c8b89a 100%)"></div>

  <div class="abs label" style="left:445px;top:60px">Per existent est quod &gt;</div>
  <div class="abs rule" style="left:420px;top:92px;width:350px"></div>
  <div class="abs label" style="left:460px;top:140px">Et ipsum quodque</div>
  <p class="abs text" style="left:460px;top:175px;width:330px">Sed in dui in augue consectetur lobortis. Pellentesque orci tellus, imperdiet interdum nibh a, varius gravida augue.</p>
  <div class="photo" role="img" aria-label="Notebook and pen on a wooden table" style="left:440px;top:292px;width:350px;height:240px;background:linear-gradient(120deg,#d9dde2 0%,#b9bfc6 45%,#6b4a30 55%,#4a3322 100%)"></div>

  <div class="abs label" style="left:830px;top:60px">Et augue varius</div>
  <p class="abs text" style="left:830px;top:100px;width:330px">Sed in dui in augue consectetur lobortis. Pellentesque orci tellus, imperdiet interdum nibh a, varius gravida augue. Curabitur faucibus, lectus vitae maximus scelerisque, nunc arcu molestie erat, congue efficitur ante enim eget mi. Phasellus id felis laoreet, viverra purus eget, hendrerit nulla. Aenean interdum mollis gravida. Sed consectetur sit amet sapien vel iaculis. Phasellus iaculis dapibus ligula, non condimentum dolor semper sit amet. Aliquam ut dui et risus sagittis tincidunt at at augue. Etiam elementum lacus vulputate interdum placerat.</p>
</section>

<section class="abs welcome">
  <h2 class="script">Welcome to my site</h2>
  <p>Pellentesque habitant morbi tristique senectus et netus et malesuada fames ac turpis egestas. Curabitur est erat, eleifend ut dignissim a, imperdiet ac leo. Morbi tincidunt nulla sit massa vehicula, eu porta dolor feugiat. Lorem ipsum dolor sit amet, consectetur adipiscing elit. Donec gravida gravida leo, convallis consectetur libero pulvinar sit amet. Interdum et malesuada fames ac ante ipsum primis in faucibus. Donec quis vulputate mi.</p>
  <div class="abs more" style="left:0;width:1200px;text-align:center;top:280px">KNOW MORE</div>
</section>

<section class="abs pale">
  <h3 class="abs script" style="left:85px;top:58px;font-size:40px">Vulpus Elit</h3>
  <p class="abs text" style="left:85px;top:120px;width:490px">Quisque tincidunt quam a porta sagittis. Etiam at urna dolor. Curabitur semper, arcu ut consequat sagittis, arcu purus venenatis est, et tristique nibh nibh porttitor odio. Nunc blandit ac ante in</p>
  <p class="abs quote" style="left:88px;top:240px;width:420px">“eternatitem magistima chose perception randa quod vivendum et se quanda scit…”</p>

  <h3 class="abs script" style="left:615px;top:58px;font-size:40px">Pupit Peptlena</h3>
  <p class="abs text" style="left:615px;top:120px;width:500px">Quisque tincidunt quam a porta sagittis. Etiam at urna dolor. Curabitur semper, arcu ut consequat sagittis, arcu purus venenatis est, et tristique nibh nibh porttitor odio. Nunc blandit ac ante in</p>
  <div class="abs label" style="left:615px;top:206px;font-size:16px">Eternitatem magistima chose</div>
  <div class="photo" role="img" aria-label="Cup of tea with daisies and open papers" style="left:615px;top:255px;width:498px;height:230px;background:linear-gradient(120deg,#6a6660 0%,#a9a39a 40%,#e8e4de 70%,#c9c3bb 100%)"></div>
</section>

<section class="abs dusk" role="img" aria-label="Lake shore with trees in golden evening light">
  <div class="photo" role="img" aria-label="Stack of old books with reading glasses" style="left:36px;top:95px;width:502px;height:330px;background:linear-gradient(160deg,#e4dfd8 0%,#a89e92 40%,#4e4438 75%,#2e271f 100%)"></div>
  <div class="abs label" style="left:615px;top:52px">Tincidunt quam sert</div>
  <p class="abs text" style="left:615px;top:85px;width:520px">Quisque tincidunt quam a porta sagittis. Etiam at urna dolor. Curabitur semper, arcu ut consequat sagittis, arcu purus venenatis est, et tristique nibh nibh porttitor odio. Nunc blandit ac ante in</p>
  <div class="abs label" style="left:615px;top:198px">Et quique potest</div>
  <p class="abs text" style="left:615px;top:231px;width:520px">Quisque tincidunt quam a porta sagittis. Etiam at urna dolor. Curabitur semper, arcu ut consequat sagittis, arcu purus venenatis est, et tristique nibh nibh porttitor odio. Nunc blandit ac ante in</p>
  <div class="abs label" style="left:615px;top:343px">Perpendiculae vitae</div>
  <p class="abs text" style="left:615px;top:376px;width:520px">Quisque tincidunt quam a porta sagittis. Etiam at urna dolor. Curabitur semper, arcu ut consequat sagittis, arcu purus venenatis est, et tristique nibh nibh porttitor odio. Nunc blandit ac ante in</p>
</section>

<section class="abs tan">
  <h3 class="abs script" style="left:88px;top:48px;font-size:42px">Per sciend scit</h3>
  <p class="abs text" style="left:88px;top:115px;width:440px">Sed in dui in augue consectetur lobortis. Pellentesque orci tellus, imperdiet interdum nibh a, varius gravida augue. Curabitur faucibus, lectus vitae maximus scelerisque, nunc arcu molestie erat, congue efficitur</p>
  <h3 class="abs script" style="left:88px;top:258px;font-size:42px">Quod melius</h3>
  <p class="abs text" style="left:88px;top:322px;width:440px">Sed in dui in augue consectetur lobortis. Pellentesque orci tellus, imperdiet interdum nibh a, varius gravida augue. Curabitur faucibus, lectus vitae maximus scelerisque, nunc arcu molestie erat, congue efficitur ante enim eget mi. Phasellus id felis</p>

  <div class="photo" role="img" aria-label="Coffee cup beside a stack of books on a windowsill" style="left:643px;top:30px;width:497px;height:183px;background:linear-gradient(110deg,#8a6f62 0%,#c9c0c4 35%,#e6e8ee 60%,#8f98a8 100%)"></div>
  <h3 class="abs script" style="left:643px;top:240px;font-size:42px">Magis nihil verindum</h3>
  <p class="abs text" style="left:643px;top:302px;width:500px">Quisque tincidunt quam a porta sagittis. Etiam at urna dolor. Curabitur semper, arcu ut consequat sagittis, arcu purus venenatis est, et tristique nibh nibh porttitor odio. Nunc blandit ac ante in accumsan. Vestibulum ac tincidunt eros. Suspendisse elementum</p>
  <div class="abs more" style="left:643px;top:440px">KNOW MORE</div>
</section>

<div class="abs band"></div>
<footer class="abs footer">
  <div class="abs logo script">Everett Lane Corbin</div>
  <p class="abs ftext" style="left:92px;top:142px;width:220px;line-height:30px">Lipsum quosque 10, et per 23, perque, Et sit</p>
  <div class="abs ftext" style="left:92px;top:225px;font-size:11px">SEE ON MAPS</div>

  <div class="abs fhead" style="left:448px;top:80px">Links</div>
  <ul class="abs flist" style="left:448px;top:120px">
    <li>Home</li><li>Portfolio</li><li>Services</li><li>About</li><li>Contact</li>
  </ul>

  <div class="abs fhead" style="left:625px;top:80px">About us</div>
  <p class="abs ftext" style="left:625px;top:120px;width:220px">Suspendisse aliquet purus et lectus consequat, vel auctor ante auctor. Nam et sapien</p>
  <div class="abs ftext" style="left:625px;top:225px;font-size:11px">READ MORE</div>

  <div class="abs fhead" style="left:975px;top:80px">More</div>
  <ul class="abs flist" style="left:975px;top:120px">
    <li>Pharetra</li><li>Ecit</li><li>Perque</li><li>Ed sae</li><li>Quoque</li>
  </ul>
</footer>

</body>
</html>
```